QRV Business Cards

We are looking for innovative edits to freshen up the card we uploaded. Several examples to choose from will be very helpful. Once we get this decided we will need cards for approximately 20 people.

From the BC attached you will see most of the content we want to keep, we are looking for layout options..the Logo must stay red/blue everything else may be changed to enhance.

Each employee will have their picture on the card.
Updates

Target Market(s)

B2B and Government agencies

Industry/Entity Type

Business

Contact Information for Business Card

This is a double sided fold over business card.

Requirements
Must have
• LOGO - same color and format
• LED Lighting Solutions w/Design, Installation, Financing as a stand out
Nice to have
• We had a cartoon charter drawn but I'm not sure if he will fit the card or not...just providing an idea.

```html
<!DOCTYPE html>
<html lang="en">
<head>
<meta charset="utf-8">
<title>QRV Lighting – Fold-over Business Card</title>
<link href="https://fonts.googleapis.com/css2?family=Source+Sans+3:wght@400;600;700;800&display=swap" rel="stylesheet">
<style>
  :root{
    --stage:#0f1315;
    --paper:#f1efe9;
    --red:#d6202f;
    --blue:#2b3a8c;
    --ink:#1d1d1d;
    --label:#b9bcbe;
    --white:#ffffff;
  }
  *{box-sizing:border-box;margin:0;padding:0}
  html,body{width:1000px;height:1200px;overflow:hidden}
  body{background:var(--stage);font-family:"Source Sans 3",Arial,sans-serif;position:relative}

  .side-label{position:absolute;color:var(--label);font-size:17px;letter-spacing:3px;white-space:nowrap;transform-origin:center}
  .side-label.left{transform:translate(-50%,-50%) rotate(-90deg)}
  .side-label.right{transform:translate(-50%,-50%) rotate(90deg)}

  .panel{position:absolute;width:420px;height:238px;background:var(--paper);overflow:hidden}
  .panel svg.bands{position:absolute;inset:0}

  .wordmark{color:var(--red);font-weight:800;text-transform:uppercase;line-height:.9;letter-spacing:1px}

  /* Front */
  .front .wordmark{position:absolute;left:0;right:0;top:58px;text-align:center;font-size:64px}

  /* Back */
  .back .wordmark{position:absolute;left:18px;top:20px;font-size:34px}
  .back .person{position:absolute;left:16px;top:112px}
  .back .name{font-size:15px;font-weight:600;color:var(--ink)}
  .back .title{font-size:11px;color:var(--ink)}
  .back .contacts{position:absolute;left:18px;top:154px;font-size:10px;color:var(--ink);line-height:13.5px}
  .contacts li{list-style:none;display:flex;align-items:center;gap:5px}
  .contacts li.gap{margin-top:6px}
  .contacts svg{width:8px;height:8px;flex:none}
  .back .portrait{position:absolute;right:0;top:0;width:160px;height:238px;
    background:linear-gradient(180deg,#e8e4dc 0%,#c9a58e 38%,#3a3a40 62%,#1c1d22 100%)}

  /* Internal 1 */
  .licences{position:absolute;left:28px;top:66px;font-size:11px;font-weight:700;color:var(--ink);line-height:14px;text-align:center;width:100px}
  .licences p+p{margin-top:12px}
  .services{position:absolute;right:14px;top:18px;text-align:right;color:var(--white)}
  .services h3{font-size:14px;font-weight:600;margin-bottom:3px}
  .services p{font-size:11.5px;line-height:20px}
  .services h3.second{margin-top:13px}

  /* Internal 2 */
  .offer{position:absolute;left:0;top:22px;width:206px;text-align:center;color:var(--white)}
  .offer h3{font-size:16px;font-weight:600}
  .offer h3 b{font-weight:800}
  .offer .site{font-size:11px;font-weight:600}
  .offer ul{list-style:none;margin-top:18px;font-size:18px;color:#e9e3d4}
  .offer li.dot{font-size:10px;line-height:14px}
  .offer li.step{line-height:24px}
  .centers{position:absolute;left:256px;width:150px;top:30px;text-align:center;color:var(--ink)}
  .centers h3{font-size:12.5px;font-weight:700}
  .centers h4{font-size:15px;font-weight:700;margin-top:16px;margin-bottom:2px}
  .centers p{font-size:11px;line-height:14px}
</style>
</head>
<body>

  <span class="side-label left" style="left:22px;top:466px">FRONT &nbsp;⟲180°</span>
  <span class="side-label left" style="left:22px;top:734px">BACK</span>
  <span class="side-label right" style="left:976px;top:466px">INTERNAL 1</span>
  <span class="side-label right" style="left:976px;top:734px">INTERNAL 2</span>

  <!-- Front -->
  <section class="panel front" style="left:42px;top:347px">
    <div class="wordmark">QRV<br>Lighting</div>
  </section>

  <!-- Internal 1 -->
  <section class="panel internal-one" style="left:536px;top:347px">
    <svg class="bands" viewBox="0 0 420 238" aria-hidden="true">
      <polygon points="146,0 166,0 228,238 222,238" fill="var(--blue)"/>
      <polygon points="172,0 420,0 420,238 234,238" fill="var(--red)"/>
    </svg>
    <div class="licences">
      <p>VA 1104 5521 08B<br>MD 0417 3380</p>
      <p>DC ECC7001426<br>D2 1009338721</p>
      <p>MDOT #04-227<br>VDOT #518093</p>
    </div>
    <div class="services">
      <h3>24 Hour Emergency Services</h3>
      <p>Directional Drilling • Electrical Services</p>
      <p>Energy Audits • Night Inspections</p>
      <p>Parking Lot Lighting • Pole Inspections</p>
      <h3 class="second">Roadway Lighting</h3>
      <p>Sign Services • Sports Lighting</p>
      <p>Stray Voltage Testing</p>
      <p>Traffic Signals • Utility Locating</p>
      <p>Vacuum Excavation</p>
    </div>
  </section>

  <!-- Back -->
  <section class="panel back" style="left:42px;top:615px">
    <div class="portrait" role="img" aria-label="Employee portrait photograph"></div>
    <div class="wordmark">QRV<br>Lighting</div>
    <div class="person">
      <p class="name">Dana Whitfield</p>
      <p class="title">Chief Executive Officer</p>
    </div>
    <ul class="contacts">
      <li><svg viewBox="0 0 8 8"><rect x="2" y="0.5" width="4" height="7" rx="0.8" fill="none" stroke="var(--red)" stroke-width="1"/></svg>410-555-0148</li>
      <li><svg viewBox="0 0 8 8"><rect x="2" y="0" width="4" height="3" fill="var(--red)"/><rect x="0" y="3" width="8" height="4" rx="1" fill="var(--red)"/></svg>877-555-0162</li>
      <li><svg viewBox="0 0 8 8"><path d="M0 3 Q4 0 8 3 L7 4 L5.5 3.2 L2.5 3.2 L1 4Z" fill="var(--red)"/><rect x="1.5" y="4.5" width="5" height="3" rx="0.8" fill="var(--red)"/></svg>877-555-0170 x214</li>
      <li class="gap"><svg viewBox="0 0 8 8"><path d="M4 8 L1.3 4 A3 3 0 1 1 6.7 4Z" fill="var(--red)"/><circle cx="4" cy="3" r="1" fill="var(--paper)"/></svg>418 B Harbor Rd., Westbrook MD 21990</li>
      <li><svg viewBox="0 0 8 8"><rect x="0" y="1.5" width="8" height="5" fill="var(--red)"/><path d="M0 1.5 L4 4.5 L8 1.5" fill="none" stroke="var(--paper)" stroke-width="0.8"/></svg>DWhitfield@QRVLighting.com</li>
    </ul>
  </section>

  <!-- Internal 2 -->
  <section class="panel internal-two" style="left:536px;top:615px">
    <svg class="bands" viewBox="0 0 420 238" aria-hidden="true">
      <polygon points="0,0 212,0 178,238 0,238" fill="var(--blue)"/>
      <polygon points="240,0 264,0 196,238 184,238" fill="var(--red)"/>
    </svg>
    <div class="offer">
      <h3>Turn-Key <b>LED</b> Solutions</h3>
      <p class="site">www.QRVLighting.com</p>
      <ul>
        <li class="step">DESIGN</li>
        <li class="dot">●</li>
        <li class="step">INSTALLATION</li>
        <li class="dot">●</li>
        <li class="step">FINANCING</li>
      </ul>
    </div>
    <div class="centers">
      <h3>OPERATION CENTERS</h3>
      <h4>MARYLAND</h4>
      <p>FAIRHOLM<br>BROOKDALE<br>ELMWOOD</p>
      <h4>VIRGINIA</h4>
      <p>CEDAR POINT<br>OAKRIDGE<br>PINEVIEW</p>
    </div>
  </section>

</body>
</html>
```